Employee Portal UI Design - Modern and Clean

We are an agency tasked with developing a team portal for a company that has many employees. As we embark on this project, we seek a great UI design to accompany the requirements our client has for this project. We already have several screens mocked up that can be used as reference for the overall idea. Currently, we are only looking for the main dashboard's home page, user registration screen, and account settings page to be designed. The main brand colors are red but other accents can be used as well. The client's vision is for modern & minimalist to be at the center. We have a specific font to be used, but if you don't have access to it, you can just use a similar font.Main color: #DD0031The sub menus (do not need to be designed) would be:>Performance Reviews>Posts>Team directory>Calendar>Tasks>Documents>LinksWe would prefer the design be made in Adobe XD.

Industry/Entity Type

Fast Food Restaurant

Number of Pages Required

1 page

Font styles to use
Sans Serif

Colors
ec1f27

Requirements
Must have
• Color: #DD0031 (highlights)

```html
<!DOCTYPE html>
<html lang="en">
<head>
<meta charset="utf-8">
<title>Team Portal – Dashboard, Registration and Settings</title>
<link href="https://fonts.googleapis.com/css2?family=Roboto:wght@300;400;500;700&display=swap" rel="stylesheet">
<style>
:root{
  --red:#e8202a;
  --orange:#f0701e;
  --amber:#f5a21f;
  --ink:#1d1d1d;
  --text:#333;
  --muted:#9a9a9a;
  --faint:#bdbdbd;
  --canvas:#efe9e6;
  --strip:#f1ece9;
  --field:#f4f2f1;
  --line:#e6e1de;
  --white:#fff;
  --btn-grey:#7c7977;
  --dark:#222;
}
*{box-sizing:border-box;margin:0;padding:0}
html,body{width:1200px;height:1200px;overflow:hidden;background:var(--white);font-family:'Roboto',Arial,sans-serif;color:var(--text)}
.stage{position:absolute;left:0;top:0;width:1500px;height:1500px;transform:scale(.8);transform-origin:0 0}
.side-strip{position:absolute;left:0;top:0;width:404px;height:1500px;background:var(--strip)}
.screen{position:absolute;width:920px;height:576px;border-radius:40px;background:var(--canvas);overflow:hidden;box-shadow:0 18px 40px rgba(60,40,30,.10)}
.topbar{position:absolute;left:0;top:0;width:100%;height:52px;background:var(--white)}
.abs{position:absolute}
.icon{fill:none;stroke:currentColor;stroke-width:1.6;stroke-linecap:round;stroke-linejoin:round}
.hamburger{left:70px;top:22px;width:20px;height:14px;color:#444}
.logo-pill{top:13px;left:280px;width:100px;height:30px;border-radius:6px;background:#ebe5e2;color:#888;font-size:12px;display:flex;align-items:center;justify-content:center;letter-spacing:.5px}
.dots{width:18px;height:6px;color:#555}
.bell{width:16px;height:18px;color:#666}
.bell-dot{width:6px;height:6px;border-radius:50%;background:var(--red)}
.avatar{width:30px;height:30px;border-radius:4px;background:linear-gradient(135deg,#55606b,#9aa3a8 60%,#39434d)}
.avatar.guest{background:#e6e3e1}
.user-name{font-size:12px;color:#222;top:21px}
.caret{width:10px;height:8px;fill:var(--red)}

.sidebar{position:absolute;left:44px;top:95px;width:70px}
.nav-item{width:70px;height:50px;margin-bottom:8px;border-radius:7px;background:var(--white);display:flex;flex-direction:column;align-items:center;justify-content:center;font-size:8.5px;color:#777;box-shadow:0 1px 3px rgba(0,0,0,.05)}
.nav-item svg{width:15px;height:15px;color:#666;margin-bottom:4px}
.nav-item.active{background:var(--red);color:var(--white);font-weight:500}
.nav-item.active svg{color:var(--white)}

.page-title{position:absolute;font-size:16px;font-weight:700;color:var(--ink)}
.tool-btn{position:absolute;top:95px;width:86px;height:50px;border-radius:6px;background:var(--btn-grey);color:var(--white);font-size:8.5px;display:flex;align-items:center;justify-content:center;gap:8px}
.tool-btn svg{width:14px;height:14px}

.card{position:absolute;background:var(--white);border-radius:4px}
.activity{position:absolute;left:0;width:362px;padding:20px 13px 0 13px;border-bottom:1px solid var(--line)}
.activity:last-child{border-bottom:none}
.act-head{display:flex;align-items:center;font-size:8.5px;color:var(--faint)}
.act-avatar{width:18px;height:18px;border-radius:3px;background:linear-gradient(135deg,#55606b,#a0a8ad);margin-right:8px}
.act-date{margin-left:auto;color:var(--faint)}
.act-date b{font-weight:400;color:#777}
.act-title{margin-top:8px;font-size:12.5px;font-weight:700;color:var(--red)}
.act-sub{margin-top:4px;font-size:10px;color:#333}
.act-body{margin-top:10px;font-size:8.3px;line-height:13px;color:var(--faint)}

.cal-head{position:absolute;top:12px;left:0;width:321px;text-align:center;font-size:12px;color:var(--red)}
.cal-arrow{position:absolute;top:15px;width:7px;height:9px;fill:var(--red)}
.cal-grid{position:absolute;left:10px;top:42px;display:grid;grid-template-columns:repeat(7,43px);grid-auto-rows:25px;font-size:8.5px;color:#444;text-align:center}
.cal-grid .dow{color:var(--faint)}
.cal-grid .off{color:var(--faint)}
.day{position:relative;line-height:14px}
.day .today{display:inline-block;width:18px;height:18px;line-height:18px;border-radius:50%;background:var(--red);color:var(--white);margin-top:-2px}
.marks{position:absolute;left:0;right:0;top:13px;display:flex;justify-content:center;gap:2px}
.ev{width:4px;height:4px;border-radius:50%;background:var(--orange)}
.tk{width:5px;height:5px;border-radius:50%;border:1px solid var(--amber)}
.legend{position:absolute;top:198px;font-size:8px;display:flex;align-items:center;gap:8px}
.cal-divider{position:absolute;left:0;top:218px;width:321px;height:2px;background:var(--canvas)}
.cal-split{position:absolute;left:159px;top:218px;width:2px;height:242px;background:var(--canvas)}
.agenda{position:absolute;top:230px;width:150px}
.agenda h4{font-size:11px;font-weight:500;color:var(--ink);margin-bottom:12px}
.agenda .when{font-size:11px;margin-bottom:11px}
.agenda .when small{font-size:8px}
.agenda .item{position:relative;margin-bottom:10px;font-size:8px;color:var(--ink);font-weight:500}
.agenda .item span{display:block;margin-top:5px;font-weight:400}
.agenda .item i{position:absolute;left:-12px;top:13px}
.agenda .more{font-size:8px;display:flex;align-items:center;gap:6px;margin-top:2px}
.events .when,.events .item span,.events .more{color:var(--orange)}
.tasks .when,.tasks .item span,.tasks .more{color:var(--amber)}

.form-panel{position:absolute;background:var(--white)}
.label{position:absolute;font-size:11px;color:var(--ink)}
.photo-slot{position:absolute;width:85px;height:85px;border-radius:5px}
.edit-btn{position:absolute;width:28px;height:28px;border-radius:5px;background:var(--dark);display:flex;align-items:center;justify-content:center;color:var(--white)}
.edit-btn svg{width:11px;height:11px}
.field{position:absolute;width:183px;height:36px;border-radius:4px;background:var(--field);border:1px solid #ebe8e6;padding:0 12px;display:flex;flex-direction:column;justify-content:center;font-size:10px;color:var(--ink)}
.field em{font-style:normal;color:var(--red)}
.field small{font-size:7.5px;color:var(--faint);margin-bottom:3px}
.divider{position:absolute;height:1px;background:var(--line)}
.primary-btn{position:absolute;width:91px;height:32px;border-radius:5px;background:var(--red);color:var(--white);font-size:12px;font-weight:500;display:flex;align-items:center;justify-content:center;box-shadow:0 3px 6px rgba(232,32,42,.25)}

.tab{position:absolute;top:94px;width:93px;height:50px;border-radius:5px 5px 0 0;background:var(--white);font-size:7.5px;color:#555;display:flex;align-items:center;justify-content:center;text-align:center}
.tab.active{height:60px;border-radius:5px 5px 0 0;align-items:flex-start;padding-top:20px}
</style>
</head>
<body>
<svg width="0" height="0" style="position:absolute">
  <defs>
    <symbol id="i-home" viewBox="0 0 16 16"><path d="M2 8 8 2.5 14 8v6H10V10H6v4H2z" fill="currentColor" stroke="none"/></symbol>
    <symbol id="i-star" viewBox="0 0 16 16"><path d="M8 1.5l2 4.3 4.6.5-3.4 3.1 1 4.6L8 11.6 3.8 14l1-4.6L1.4 6.3 6 5.8z" fill="currentColor" stroke="none"/></symbol>
    <symbol id="i-pen" viewBox="0 0 16 16"><path d="M3 13l1-3.5 7-7 2.5 2.5-7 7z" fill="currentColor" stroke="none"/><path d="M2 14.5h5" stroke="currentColor" stroke-width="1"/></symbol>
    <symbol id="i-team" viewBox="0 0 16 16"><g fill="currentColor"><circle cx="8" cy="3" r="1.8"/><circle cx="3" cy="12" r="1.8"/><circle cx="13" cy="12" r="1.8"/></g><path d="M8 5v3M3 10V8h10v2" fill="none" stroke="currentColor" stroke-width="1.2"/></symbol>
    <symbol id="i-cal" viewBox="0 0 16 16"><rect x="2" y="3" width="12" height="11" fill="none" stroke="currentColor" stroke-width="1.3"/><path d="M2 6.5h12M6 3v11M10 3v11M2 10h12M5 1.5v2M11 1.5v2" stroke="currentColor" stroke-width="1.1"/></symbol>
    <symbol id="i-folder" viewBox="0 0 16 16"><path d="M1.5 4h5l1.5 1.5h6.5V13h-13z" fill="currentColor" opacity=".35"/><path d="M1.5 13l2-6h11l-2 6z" fill="currentColor"/></symbol>
    <symbol id="i-doc" viewBox="0 0 16 16"><path d="M3.5 1.5h6l3 3v10h-9z M9.5 1.5v3h3 M5.5 8h5M5.5 10.5h5" fill="none" stroke="currentColor" stroke-width="1.1"/></symbol>
    <symbol id="i-link" viewBox="0 0 16 16"><path d="M6.5 9.5l3-3M7 4.5l1.5-1.5a2.5 2.5 0 0 1 3.5 3.5L10.5 8M9 11.5 7.5 13A2.5 2.5 0 0 1 4 9.5L5.5 8" fill="none" stroke="currentColor" stroke-width="1.2" stroke-linecap="round"/></symbol>
    <symbol id="i-bell" viewBox="0 0 16 18"><path d="M8 1.5a5 5 0 0 0-5 5v4.5L1.5 13h13L13 11V6.5a5 5 0 0 0-5-5z M6 15a2 2 0 0 0 4 0z" fill="currentColor"/></symbol>
    <symbol id="i-dots" viewBox="0 0 18 6"><g fill="currentColor"><circle cx="3" cy="3" r="2"/><circle cx="9" cy="3" r="2"/><circle cx="15" cy="3" r="2"/></g></symbol>
    <symbol id="i-menu" viewBox="0 0 20 14"><path d="M1 2h18M1 12h13" stroke="currentColor" stroke-width="2.2" stroke-linecap="round"/></symbol>
    <symbol id="i-caret" viewBox="0 0 10 8"><path d="M0 0h10L5 8z"/></symbol>
    <symbol id="i-edit" viewBox="0 0 12 12"><path d="M2 10l.7-2.6 5.5-5.5 1.9 1.9-5.5 5.5z M7.3 2.8l1.9 1.9" fill="none" stroke="currentColor" stroke-width="1"/></symbol>
    <symbol id="i-arrow" viewBox="0 0 18 6"><path d="M0 3h16M13 .5 16.5 3 13 5.5" fill="none" stroke="currentColor" stroke-width="1"/></symbol>
  </defs>
</svg>

<div class="stage">
  <div class="side-strip"></div>

  <!-- Registration screen -->
  <section class="screen registration" style="left:518px;top:463px;">
    <div class="topbar">
      <svg class="abs dots" style="left:575px;top:25px"><use href="#i-dots"/></svg>
      <svg class="abs bell" style="left:620px;top:19px"><use href="#i-bell"/></svg>
      <span class="abs bell-dot" style="left:631px;top:17px"></span>
      <div class="abs avatar guest" style="left:699px;top:13px" role="img" aria-label="Guest avatar placeholder"></div>
      <span class="abs user-name" style="left:739px;top:22px">Guest</span>
      <svg class="abs caret" style="left:845px;top:24px"><use href="#i-caret"/></svg>
    </div>
    <nav class="sidebar" style="top:147px;left:45px">
      <div class="nav-item"><svg><use href="#i-star"/></svg>Reviews</div>
      <div class="nav-item"><svg><use href="#i-pen"/></svg>Posts</div>
      <div class="nav-item"><svg><use href="#i-team"/></svg>Team Directory</div>
      <div class="nav-item"><svg><use href="#i-cal"/></svg>Calendar</div>
      <div class="nav-item"><svg><use href="#i-folder"/></svg>Tasks</div>
    </nav>
    <div class="form-panel" style="left:164px;top:153px;width:718px;height:400px">
      <span class="label" style="left:48px;top:30px">Profile Picture</span>
      <div class="photo-slot" style="left:48px;top:64px;background:#f2f0ef;border:1px solid #e6e2e0;overflow:hidden">
        <svg width="85" height="85" viewBox="0 0 85 85"><circle cx="42" cy="36" r="17" fill="#d9d6d4"/><path d="M12 85c2-20 14-28 30-28s28 8 30 28z" fill="#d9d6d4"/></svg>
      </div>
      <div class="edit-btn" style="left:117px;top:50px"><svg><use href="#i-edit"/></svg></div>
      <span class="label" style="left:206px;top:30px">Personal Information</span>
      <div class="field" style="left:206px;top:58px">Name <em></em></div>
      <div class="field" style="left:482px;top:58px">Last Name</div>
      <div class="field" style="left:206px;top:115px">Email Address</div>
      <div class="field" style="left:482px;top:115px">Phone Number</div>
      <div class="field" style="left:206px;top:172px">City</div>
      <div class="field" style="left:482px;top:172px">State</div>
      <div class="divider" style="left:206px;top:232px;width:459px"></div>
      <div class="field" style="left:482px;top:279px">Password</div>
      <div class="primary-btn" style="left:574px;top:340px">Sign up</div>
    </div>
  </section>

  <!-- Dashboard home -->
  <section class="screen dashboard" style="left:75px;top:60px;">
    <div class="topbar">
      <svg class="abs hamburger"><use href="#i-menu"/></svg>
      <div class="abs logo-pill">LOGO</div>
      <svg class="abs dots" style="left:578px;top:26px"><use href="#i-dots"/></svg>
      <svg class="abs bell" style="left:624px;top:20px"><use href="#i-bell"/></svg>
      <div class="abs avatar" style="left:704px;top:14px" role="img" aria-label="User profile photo"></div>
      <span class="abs user-name" style="left:744px">Alex Moreno</span>
      <svg class="abs caret" style="left:851px;top:25px"><use href="#i-caret"/></svg>
    </div>
    <nav class="sidebar">
      <div class="nav-item active"><svg><use href="#i-home"/></svg>Home</div>
      <div class="nav-item"><svg><use href="#i-star"/></svg>Reviews</div>
      <div class="nav-item"><svg><use href="#i-pen"/></svg>Posts</div>
      <div class="nav-item"><svg><use href="#i-team"/></svg>Team Directory</div>
      <div class="nav-item"><svg><use href="#i-cal"/></svg>Calendar</div>
      <div class="nav-item"><svg><use href="#i-folder"/></svg>Tasks</div>
      <div class="nav-item"><svg><use href="#i-doc"/></svg>Documents</div>
      <div class="nav-item"><svg><use href="#i-link"/></svg>Links</div>
    </nav>
    <h2 class="page-title" style="left:159px;top:111px">Recent Activities</h2>
    <div class="tool-btn" style="left:340px"><svg class="icon" viewBox="0 0 14 14"><circle cx="6" cy="6" r="4.3"/><path d="M9.2 9.2 13 13"/></svg>Search...</div>
    <div class="tool-btn" style="left:435px"><svg class="icon" viewBox="0 0 14 14" style="stroke-width:2"><path d="M7 1v12M1 7h12"/></svg>Add Post</div>

    <div class="card activities" style="left:159px;top:153px;width:362px;height:402px">
      <article class="activity" style="top:0;height:130px">
        <div class="act-head"><span class="act-avatar"></span>Alex Moreno<span class="act-date">Friday 01.03, <b>11:00 AM</b></span></div>
        <div class="act-title">New Performance Review</div>
        <div class="act-sub">Performance Review for Alex Moreno</div>
        <p class="act-body">Lorem ipsum dolor sit amet, consectetur adipiscing elit, sed do eiusmod tempor incididunt ut labore et dolore magna aliqua. Ut enim ad minim veniam, quis nostrud</p>
      </article>
      <article class="activity" style="top:130px;height:128px">
        <div class="act-head"><span class="act-avatar"></span>Alex Moreno<span class="act-date">Friday 01.03, <b>11:00 AM</b></span></div>
        <div class="act-title">New Performance Review</div>
        <div class="act-sub">Performance Review for Alex Moreno</div>
        <p class="act-body">Lorem ipsum dolor sit amet, consectetur adipiscing elit, sed do eiusmod tempor incididunt ut labore et dolore magna aliqua. Ut enim ad minim veniam, quis nostrud</p>
      </article>
      <article class="activity" style="top:258px;height:144px;padding-top:16px">
        <div class="act-head"><span class="act-avatar"></span>Alex Moreno<span class="act-date">Friday 01.03, <b>11:00 AM</b></span></div>
        <div class="act-title">New Performance Review</div>
        <div class="act-sub">Performance Review for Alex Moreno</div>
        <p class="act-body">Lorem ipsum dolor sit amet, consectetur adipiscing elit, sed do eiusmod tempor incididunt ut labore et dolore magna aliqua. Ut enim ad minim veniam, quis nostrud exercitation ullamco laboris nisi ut aliquip ex ea commodo consequat.</p>
      </article>
    </div>

    <div class="card calendar" style="left:565px;top:95px;width:321px;height:460px">
      <svg class="cal-arrow" style="left:13px"><path d="M7 0v9L0 4.5z"/></svg>
      <div class="cal-head">March 2019</div>
      <svg class="cal-arrow" style="left:289px"><path d="M0 0v9l7-4.5z"/></svg>
      <div class="cal-grid">
        <div class="dow">M</div><div class="dow">T</div><div class="dow">W</div><div class="dow">T</div><div class="dow">F</div><div class="dow">S</div><div class="dow">S</div>
        <div class="day off">25</div><div class="day off">26</div><div class="day off">27</div><div class="day off">28</div><div class="day">1</div><div class="day">2</div><div class="day"><span class="today">3</span></div>
        <div class="day">4<span class="marks"><i class="ev"></i><i class="tk"></i></span></div>
        <div class="day">5<span class="marks"><i class="ev"></i><i class="tk"></i></span></div>
        <div class="day">6<span class="marks"><i class="tk"></i></span></div>
        <div class="day">7<span class="marks"><i class="ev"></i></span></div>
        <div class="day">8</div>
        <div class="day">9<span class="marks"><i class="tk"></i></span></div>
        <div class="day">10<span class="marks"><i class="ev"></i></span></div>
        <div class="day">11</div>
        <div class="day">12<span class="marks"><i class="ev"></i><i class="tk"></i></span></div>
        <div class="day">13</div><div class="day">14</div>
        <div class="day">15<span class="marks"><i class="ev"></i></span></div>
        <div class="day">16</div><div class="day">17</div>
        <div class="day">18</div><div class="day">19</div>
        <div class="day">20<span class="marks"><i class="ev"></i><i class="tk"></i></span></div>
        <div class="day">21</div><div class="day">22</div><div class="day">23</div><div class="day">24</div>
        <div class="day">25</div><div class="day">26</div><div class="day">27</div><div class="day">28</div><div class="day">29</div><div class="day">30</div><div class="day">31</div>
      </div>
      <div class="legend" style="left:37px;color:var(--orange)"><i class="ev"></i>Events</div>
      <div class="legend" style="left:185px;color:var(--amber)"><i class="tk"></i>Tasks</div>
      <div class="cal-divider"></div>
      <div class="cal-split"></div>
      <div class="agenda events" style="left:36px">
        <h4>EVENTS</h4>
        <div class="when">Tomorrow, <small>04.03</small></div>
        <div class="item"><i class="ev"></i>Daily Safe Checklist<span>8:45 AM - 9:00 AM</span></div>
        <div class="item"><i class="ev"></i>Director Meeting<span>10:00 AM - 11:00 AM</span></div>
        <div class="when" style="margin-top:18px">Tuesday, <small>05.03</small></div>
        <div class="item"><i class="ev"></i>Daddy Daughter Night<span>8:45 AM - 9:00 AM</span></div>
        <div class="more">See more <svg width="18" height="6"><use href="#i-arrow"/></svg></div>
      </div>
      <div class="agenda tasks" style="left:185px">
        <h4>TASKS</h4>
        <div class="when">Tomorrow, <small>04.03</small></div>
        <div class="item"><i class="tk"></i>Daily Stand-Up<span>8:45 AM - 9:00 AM</span></div>
        <div class="item"><i class="tk"></i>Daily eRQA<span>10:00 AM - 11:00 AM</span></div>
        <div class="when" style="margin-top:18px">Tuesday, <small>05.03</small></div>
        <div class="item"><i class="tk"></i>Daily Safe Checklist<span>8:45 AM - 9:00 AM</span></div>
        <div class="more">See more <svg width="18" height="6"><use href="#i-arrow"/></svg></div>
      </div>
    </div>
  </section>

  <!-- Account settings -->
  <section class="screen settings" style="left:290px;top:864px;">
    <div class="topbar">
      <svg class="abs hamburger"><use href="#i-menu"/></svg>
      <div class="abs logo-pill" style="left:278px">LOGO</div>
      <svg class="abs dots" style="left:573px;top:26px"><use href="#i-dots"/></svg>
      <svg class="abs bell" style="left:619px;top:20px"><use href="#i-bell"/></svg>
      <span class="abs bell-dot" style="left:629px;top:18px"></span>
      <div class="abs avatar" style="left:698px;top:14px" role="img" aria-label="User profile photo"></div>
      <span class="abs user-name" style="left:738px;font-size:12.5px">Alex Moreno</span>
      <svg class="abs caret" style="left:844px;top:25px"><use href="#i-caret"/></svg>
    </div>
    <nav class="sidebar" style="top:94px">
      <div class="nav-item active"><svg><use href="#i-home"/></svg>Home</div>
      <div class="nav-item"><svg><use href="#i-star"/></svg>Reviews</div>
      <div class="nav-item"><svg><use href="#i-pen"/></svg>Posts</div>
      <div class="nav-item"><svg><use href="#i-team"/></svg>Team Directory</div>
      <div class="nav-item"><svg><use href="#i-cal"/></svg>Calendar</div>
      <div class="nav-item"><svg><use href="#i-folder"/></svg>Tasks</div>
      <div class="nav-item"><svg><use href="#i-doc"/></svg>Documents</div>
      <div class="nav-item"><svg><use href="#i-link"/></svg>Links</div>
    </nav>
    <h2 class="page-title" style="left:158px;top:110px">Settings</h2>
    <div class="tab active" style="left:271px">My Profile</div>
    <div class="tab" style="left:373px">Notifications</div>
    <div class="tab" style="left:475px">User Roles</div>
    <div class="tab" style="left:578px">Role Permissions</div>
    <div class="tab" style="left:680px">Custom Links</div>
    <div class="tab" style="left:782px">Plan &amp; Billing</div>

    <div class="form-panel" style="left:158px;top:153px;width:719px;height:403px">
      <span class="label" style="left:47px;top:30px">Profile Picture</span>
      <div class="photo-slot" style="left:47px;top:64px;background:linear-gradient(160deg,#6f7b66,#4c5a63 55%,#2e3d52)" role="img" aria-label="Profile photo of the user"></div>
      <div class="edit-btn" style="left:117px;top:50px"><svg><use href="#i-edit"/></svg></div>
      <span class="label" style="left:211px;top:30px">Personal Information</span>
      <div class="field" style="left:211px;top:58px"><small>Name:</small>Alex</div>
      <div class="field" style="left:487px;top:58px"><small>Last Name:</small>Moreno</div>
      <div class="field" style="left:211px;top:115px"><small>Email:</small>alex.moreno@mailbox.test</div>
      <div class="field" style="left:487px;top:115px"><small>Phone Number:</small>(+10) 555 010 222</div>
      <div class="field" style="left:211px;top:172px"><small>City:</small>Miami</div>
      <div class="field" style="left:487px;top:172px"><small>State:</small>Florida</div>
      <div class="divider" style="left:211px;top:232px;width:459px"></div>
      <span class="label" style="left:211px;top:251px">Change Password</span>
      <div class="field" style="left:211px;top:279px"><small>Current Password</small>**********</div>
      <div class="field" style="left:487px;top:279px"><small>New Password</small>**********</div>
      <div class="primary-btn" style="left:579px;top:340px">Save</div>
    </div>
  </section>
</div>
</body>
</html>
```